Create a web design for a vehicle codes lookup website

Create a bright and fun web design to replace our current boring one!

-Make a new design for this page that shows vehicle codes information: http://plinkor.net/vin/mara-dulek.4182.html
-Click "Random VIN" to see more examples.
-The page shows the vehicle information (see above example) is the most important one to add a redesign to. Bonus points if you create a redesign for the main page as well: plinkor.net.

Number of Pages Required

2 page

Requirements
Must have
• Be fun and have bright colors!
Should not have
• Do not add pictures of specific people or vehicles unless they can be used on every page. The example page has a Brevik Solano, but do not add a picture of the Brevik Solano because other pages have different vehicles.

```html
<!DOCTYPE html>
<html lang="en">
<head>
<meta charset="utf-8">
<title>Plinkor.net – Vehicle Purchase Records Data Search</title>
<link rel="stylesheet" href="https://fonts.googleapis.com/css2?family=Merriweather:wght@700;900&family=Lato:wght@400;700;900&display=swap">
<style>
  :root{
    --ink:#1f1f1f;
    --text:#555555;
    --dark-box:#2b2b2b;
    --orange:#f7931e;
    --red:#c0321a;
    --blue:#2c3fc4;
    --footer:#1c1c1c;
    --footer-line:#3a3a3a;
    --muted:#9a9a9a;
    --white:#ffffff;
  }
  *{box-sizing:border-box;margin:0;padding:0}
  html,body{width:1200px;height:2252px;overflow:hidden;background:var(--white)}
  body{position:relative;font-family:"Lato",sans-serif;color:var(--ink)}

  .site-header{position:absolute;top:0;left:0;width:1200px;height:70px;display:flex;align-items:center;justify-content:space-between;padding:0 84px 0 86px;z-index:3}
  .brand{font-family:"Lato",sans-serif;font-weight:700;font-size:15px;letter-spacing:1px;color:var(--ink)}
  .main-nav{display:flex;gap:30px}
  .main-nav a{font-size:11px;letter-spacing:1px;text-transform:uppercase;color:#444;text-decoration:none}

  .hero-photo{position:absolute;left:40px;top:170px;width:1120px;height:650px;
    background:radial-gradient(ellipse 60% 40% at 55% 55%,#2a2a2a 0%,#4a4a4a 35%,#dcdcdc 70%,#f6f6f6 100%);}
  .hero-title{position:absolute;left:86px;top:150px;font-family:"Merriweather",serif;font-weight:900;font-size:48px;line-height:60px;text-transform:uppercase;color:var(--ink);z-index:2;letter-spacing:.5px}

  .search-bar{position:absolute;top:800px;left:226px;display:flex;gap:22px}
  .search-bar input{width:276px;height:60px;border:1px solid #b9b9b9;padding:0 18px;font-family:"Lato",sans-serif;font-size:15px;color:#777;background:var(--white)}
  .search-bar button{width:155px;height:60px;border:0;background:var(--red);color:var(--white);font-family:"Lato",sans-serif;font-weight:900;font-size:15px;letter-spacing:.5px}

  .section-title{position:absolute;left:86px;font-family:"Merriweather",serif;font-weight:900;font-size:25px;text-transform:uppercase;color:var(--ink)}
  .section-rule{position:absolute;left:86px;width:76px;height:10px;background:var(--blue)}

  .about-text{position:absolute;left:86px;top:1034px;width:524px;font-size:13.5px;line-height:27px;text-transform:uppercase;color:var(--text)}
  .about-photo{position:absolute;left:670px;top:900px;width:500px;height:380px;
    background:radial-gradient(ellipse 55% 35% at 50% 55%,#e0231b 0%,#c4141a 45%,#f4d6d4 75%,#ffffff 100%)}

  .tips-grid{position:absolute;left:88px;top:1472px;width:1022px;display:grid;grid-template-columns:repeat(3,320px);grid-auto-rows:208px;column-gap:31px;row-gap:24px}
  .tip{padding:46px 30px 0 40px;color:var(--white)}
  .tip--dark{background:var(--dark-box)}
  .tip--orange{background:var(--orange)}
  .tip h3{font-weight:900;font-size:30px;line-height:32px;text-transform:uppercase;margin-bottom:12px}
  .tip p{font-size:12px;line-height:17px;color:#d9d9d9}
  .tip--orange p{color:#fff3e2}
  .tip--dark h3.accent{color:var(--orange)}

  .disclaimer{position:absolute;left:88px;top:1948px;width:1024px;font-size:11.5px;line-height:18px;color:var(--text)}

  .site-footer{position:absolute;left:0;top:2068px;width:1200px;height:184px;background:var(--footer);padding:68px 112px 0}
  .footer-nav{display:flex;gap:0;border-top:1px solid var(--footer-line);border-bottom:1px solid var(--footer-line)}
  .footer-nav a{font-size:16px;letter-spacing:1px;text-transform:uppercase;color:var(--muted);text-decoration:none;padding:12px 18px;border-right:1px solid var(--footer-line)}
  .footer-nav a:last-child{border-right:0}
  .copyright{margin-top:14px;font-size:10px;letter-spacing:.5px;text-transform:uppercase;color:#777}
</style>
</head>
<body>
  <header class="site-header">
    <div class="brand">PLINKOR</div>
    <nav class="main-nav">
      <a href="#">Home</a><a href="#">Search by Owner</a><a href="#">VIN Lookup</a><a href="#">Contact Us</a><a href="#">Random VIN</a>
    </nav>
  </header>

  <div class="hero-photo" role="img" aria-label="Photograph of a classic black muscle car on a white background"></div>
  <h1 class="hero-title">Vehicle Purchase<br>Records Data Search</h1>

  <form class="search-bar">
    <input type="text" placeholder="First name">
    <input type="text" placeholder="Last name">
    <button type="button">SEARCH NOW</button>
  </form>

  <h2 class="section-title" style="top:944px">What is plinkor.net?</h2>
  <div class="section-rule" style="top:994px"></div>
  <p class="about-text">Plinkor.net is a website that provides free access to vehicle purchase records data. All information on this website is public information and as such, we believe it should be free for all to view. The data comes from dealerships and auto insurance companies for new vehicle purchases across the United States. Search by name or by VIN to find vehicle purchase information, vehicle specifics, and full ownership information.</p>
  <div class="about-photo" role="img" aria-label="Photograph of a red sports coupe"></div>

  <h2 class="section-title" style="top:1244px">Do's and Don'ts</h2>
  <div class="section-rule" style="top:1294px"></div>

  <section class="tips-grid">
    <article class="tip tip--dark"><h3>Find a Friends</h3><p>Use our records to find and reconnect with a lost friend.</p></article>
    <article class="tip tip--orange"><h3>Check Yourself Out</h3><p>Go ahead and see what information is listed under your own name.</p></article>
    <article class="tip tip--dark"><h3>About Your Neighbors</h3><p>Keep your family informed by learning about the people around you.</p></article>
    <article class="tip tip--orange"><h3>Screen Employees</h3><p>Run a quick check on applicants before making any hiring decision.</p></article>
    <article class="tip tip--dark"><h3>Stalk or Spy</h3><p>Don't stalk, spy on people, or contact them against their wishes.</p></article>
    <article class="tip tip--dark"><h3 class="accent">Steal an Identity</h3><p>Don't use any record to pretend to be someone else. It is a crime.</p></article>
  </section>

  <p class="disclaimer">DISCLAIMER: By using this site, you certify that you will use any information obtained for lawfully acceptable purposes. Information contained herein is derived from public records and may contain errors or may not be accurate or complete. Data is provided as-is without warranty of any kind. This site is not a consumer reporting agency and may not be used to make decisions about credit, employment, insurance or housing. Please verify all information independently before relying on it.</p>

  <footer class="site-footer">
    <nav class="footer-nav">
      <a href="#">Home</a><a href="#">Search by Owner</a><a href="#">VIN Lookup</a><a href="#">Complete List</a><a href="#">Contact Us</a><a href="#">Random VIN</a>
    </nav>
    <p class="copyright">© 2016 Plinkor.net. All rights reserved. Privacy Policy</p>
  </footer>
</body>
</html>
```